Toward Bright Morrow (TWBM) Business Card - company with a mission

Note* The file attached... orange with "Toward Bright MORROW" (in CAPS) is our logo. I am also open to having the text "toward bright morrow" OUTSIDE the orange round logo for business card (so yes, you may take the text out).

The info: (the following info are separate. So either you can use Martin or Helena for now, but that will be 2 separate cards, not together in one card. Thanks!!

Martin K Pardo
202.555.0183
martin@towardbrightmorrow.example
Managing Partner

Helena R Voss
202.555.0147
helena@towardbrightmorrow.example
Managing Partner

Our website: www.towardbrightmorrow.example

TWBM LLC stands for Toward Bright Morrow (non profit arm is called dawn lift foundation)—our business is based out of New York City and has a non-profit arm where for every bar of soap you purchase, we donate a bar (don’t want any designs that limits us to only soap). Currently working with South Africa. We want the focus to be organic/natural soap with a mission.

Looking for a clean, fresh design.

Industry/Entity Type

Non-Profit

Requirements
Must have
• Clean, fresh, refreshing. Design should not be too busy.

```html
<!DOCTYPE html>
<html lang="en">
<head>
<meta charset="utf-8">
<title>Toward Bright Morrow – Business Card</title>
<link rel="stylesheet" href="https://fonts.googleapis.com/css2?family=Open+Sans:wght@400;600&display=swap">
<style>
  :root {
    --backdrop: #e9e6e2;
    --charcoal: #2a2a2a;
    --charcoal-soft: #323232;
    --orange: #f2a46b;
    --cream: #f3dcc6;
    --paper: #ffffff;
    --ink: #3c3c3c;
    --white: #ffffff;
  }
  * { box-sizing: border-box; margin: 0; padding: 0; }
  html, body {
    width: 1200px; height: 619px; overflow: hidden;
    background: var(--backdrop);
    font-family: "Open Sans", Arial, sans-serif;
  }
  .canvas {
    position: relative; width: 1200px; height: 619px;
  }
  .card {
    position: absolute; top: 166px;
    width: 500px; height: 286px;
    box-shadow: 0 6px 18px rgba(0,0,0,.18);
    overflow: hidden;
  }
  /* Front */
  .card--front { left: 60px; background: var(--paper); }
  .front__band {
    position: absolute; left: 0; top: 0; bottom: 0; width: 58px;
    background: var(--charcoal);
  }
  .front__rule {
    position: absolute; left: 62px; top: 0; bottom: 0; width: 3px;
    background: var(--orange);
  }
  .brand-dot {
    position: absolute; border-radius: 50%;
    background: var(--orange);
    border: 3px solid var(--paper);
  }
  .card--front .brand-dot { left: 24px; top: 48px; width: 78px; height: 78px; }
  .brand-name {
    position: absolute; font-weight: 400; letter-spacing: .2px;
  }
  .card--front .brand-name {
    left: 112px; top: 72px; font-size: 22px; color: var(--orange);
  }
  .contact {
    position: absolute; left: 238px; top: 150px;
    color: var(--ink); font-size: 11.5px; line-height: 1.55;
  }
  .contact__name { font-size: 18px; color: var(--orange); line-height: 1.2; }
  .contact__title { font-size: 12px; margin-bottom: 3px; }
  .contact__line { display: flex; align-items: center; gap: 6px; }
  .contact__icon { width: 11px; height: 11px; flex: none; }

  /* Back */
  .card--back { left: 640px; background: var(--charcoal-soft); }
  .back__rule {
    position: absolute; top: 0; bottom: 0; width: 1.5px; background: var(--cream);
  }
  .back__rule--outer { left: 52px; }
  .back__rule--inner { left: 58px; }
  .card--back .brand-dot {
    left: 22px; top: 110px; width: 68px; height: 68px; border: none;
  }
  .card--back .brand-name {
    left: 104px; top: 128px; font-size: 20px; color: var(--white);
  }
</style>
</head>
<body>
<main class="canvas">

  <section class="card card--front" aria-label="Business card front">
    <div class="front__band"></div>
    <div class="front__rule"></div>
    <div class="brand-dot"></div>
    <div class="brand-name">towardbrightmorrow</div>

    <div class="contact">
      <div class="contact__name">Martin K Pardo</div>
      <div class="contact__title">Managing Partner</div>
      <div class="contact__line">
        <svg class="contact__icon" viewBox="0 0 12 12" aria-hidden="true">
          <circle cx="6" cy="6" r="5.3" fill="none" stroke="#f2a46b" stroke-width="1.2"/>
          <path d="M4 3.3c.4-.3.8 0 1 .5l.3.8c.1.3 0 .5-.3.7 .3.7.8 1.3 1.5 1.6.2-.3.4-.4.7-.3l.8.3c.5.2.7.6.4 1-.5.6-1.2.8-2 .4C5 7.6 4.1 6.6 3.6 5.2c-.3-.8 0-1.5.4-1.9z" fill="#f2a46b"/>
        </svg>
        <span>202.555.0183</span>
      </div>
      <div class="contact__line">
        <svg class="contact__icon" viewBox="0 0 12 12" aria-hidden="true">
          <rect x="0.5" y="2" width="11" height="8" rx="1" fill="#f2a46b"/>
          <path d="M1 2.6 6 6.6l5-4" fill="none" stroke="#fff" stroke-width="1"/>
        </svg>
        <span>martin@towardbrightmorrow.example</span>
      </div>
      <div class="contact__line">
        <svg class="contact__icon" viewBox="0 0 12 12" aria-hidden="true">
          <circle cx="6" cy="6" r="5.5" fill="#f2a46b"/>
          <path d="M.8 6h10.4M6 .6v10.8M6 .6C3.5 3 3.5 9 6 11.4M6 .6c2.5 2.4 2.5 8.4 0 10.8M1.6 3.3h8.8M1.6 8.7h8.8" fill="none" stroke="#fff" stroke-width=".7"/>
        </svg>
        <span>www.towardbrightmorrow.example</span>
      </div>
    </div>
  </section>

  <section class="card card--back" aria-label="Business card back">
    <div class="back__rule back__rule--outer"></div>
    <div class="back__rule back__rule--inner"></div>
    <div class="brand-dot"></div>
    <div class="brand-name">towardbrightmorrow</div>
  </section>

</main>
</body>
</html>
```